Restaurant Menu Design - Harbor Table Trio

We have four items that need to be presented on one page 8 x 11 size with fancy touch. We uploaded 4 photos showing each of the menu items. The photos are intended to be landscape (not portrait) so some of them will need to be turned. The photos may be trimmed if that will aid in the presentation. These are 4 of many items on our menu and these will be featured as "Harbor Table Trio" (can use the 55 MPH sign or similar concept). The wood grain table background may be changed to a solid color (such as black), so as to sharpen the presentation of the dishes. ALL FOUR PHOTOS MUST BE PRESENTED ON THE DESIGN.

Target Market(s)

restaurant customer

Requirements
Must have
• Harbor Table Trio<br/>M-F 11:45 AM to 2:00 PM<br/>$24.99 ea
Should not have
• wacky, cartoon, silly themes

```html
<!DOCTYPE html>
<html lang="en">
<head>
<meta charset="utf-8">
<title>Harbor Table Trio – Lunch Menu</title>
<link href="https://fonts.googleapis.com/css2?family=Montserrat:wght@500;600;700;800&display=swap" rel="stylesheet">
<style>
  :root {
    --board-dark: #1f1f1f;
    --board-mid: #2e2e2e;
    --board-light: #3a3a3a;
    --sun-yellow: #fcd116;
    --ink: #1c1c1c;
    --white: #ffffff;
    --plate-light: #e4e4e4;
    --plate-shade: #b9b9b9;
  }
  * { margin: 0; padding: 0; box-sizing: border-box; }
  html, body { width: 873px; height: 1200px; overflow: hidden; background: var(--board-dark); }
  .menu {
    position: relative;
    width: 873px;
    height: 1200px;
    overflow: hidden;
    font-family: "Montserrat", sans-serif;
    background: radial-gradient(ellipse at 50% 40%, var(--board-light) 0%, var(--board-mid) 45%, var(--board-dark) 100%);
  }
  .brand-badge {
    position: absolute;
    left: 243px; top: 42px;
    width: 386px; height: 382px;
    background: var(--sun-yellow);
    border-radius: 18px;
    display: flex;
    align-items: center;
    justify-content: center;
    text-align: center;
  }
  .brand-name {
    color: var(--ink);
    font-weight: 800;
    font-size: 64px;
    line-height: 1.08;
    text-transform: uppercase;
    letter-spacing: 1px;
  }
  .bracket {
    position: absolute;
    top: 485px;
    width: 52px; height: 412px;
    border: 8px solid var(--sun-yellow);
  }
  .bracket--left { left: 42px; border-right: none; }
  .bracket--right { left: 779px; border-left: none; }
  .timing-title {
    position: absolute;
    left: 0; width: 873px; top: 460px;
    text-align: center;
    color: var(--sun-yellow);
    font-weight: 700;
    font-size: 130px;
    letter-spacing: 2px;
    line-height: 1;
  }
  .timing-rule {
    position: absolute;
    left: 200px; top: 604px;
    width: 490px; height: 3px;
    background: var(--white);
  }
  .days {
    position: absolute;
    left: 0; width: 873px; top: 628px;
    text-align: center;
    color: var(--white);
    font-weight: 500;
    font-size: 58px;
    letter-spacing: 3px;
    line-height: 1;
  }
  .hours {
    position: absolute;
    left: 99px; top: 700px;
    width: 671px; height: 69px;
    background: var(--sun-yellow);
    color: var(--ink);
    font-weight: 600;
    font-size: 52px;
    letter-spacing: 1px;
    display: flex; align-items: center; justify-content: center;
  }
  .price {
    position: absolute;
    left: 0; width: 873px; top: 787px;
    text-align: center;
    color: var(--white);
    font-weight: 600;
    font-size: 104px;
    line-height: 1;
  }
  .dish-row {
    position: absolute;
    left: 17px; top: 950px;
    width: 839px;
    display: flex;
    justify-content: space-between;
  }
  .dish {
    width: 196px; height: 196px;
    border-radius: 50%;
    background: radial-gradient(circle at 45% 40%, var(--plate-light) 0%, #d2d2d2 60%, var(--plate-shade) 100%);
  }
</style>
</head>
<body>
<main class="menu">
  <div class="brand-badge">
    <span class="brand-name">Harbor<br>Table<br>Trio</span>
  </div>

  <div class="bracket bracket--left"></div>
  <div class="bracket bracket--right"></div>

  <h1 class="timing-title">TIMING</h1>
  <div class="timing-rule"></div>
  <p class="days">MONDAY TO FRIDAY</p>
  <p class="hours">11:45 AM to 2:00 PM</p>
  <p class="price">$24.99 ea</p>

  <div class="dish-row">
    <div class="dish" role="img" aria-label="Photo of a plated tempura roll with salad and dipping sauce"></div>
    <div class="dish" role="img" aria-label="Photo of a bowl of udon noodle soup with fish cake and tempura"></div>
    <div class="dish" role="img" aria-label="Photo of sliced sashimi on a long white plate"></div>
    <div class="dish" role="img" aria-label="Photo of the fourth featured lunch dish on a white plate"></div>
  </div>
</main>
</body>
</html>
```